Stationery Design Project - Tax Professionals/Chartered Accountants

The name of our firm is “Penwick Group” and our slogan is “Bright Pathways”. You can also use the name "The Penwick Group" if it works better.

We are looking for a full stationery design: Letterhead, Business Card and With Compliments slip

We are looking for a bold, modern and clean/simple design that makes us stand out. We stand out as professionals in the industry and would like the stationery that our clients see to convey this image as well.

There is no colour preference.

We have used a "Lion" as our logo/symbol and that has received positive feedback from our clients; if you think the lion works then please incorporate the "lion".

If you think another symbol works then please submit this we are very open to ideas and would like to see designs that don't incorporate a lion as well.

We would like a corporate feel to this.

You could also incorporate the LG logo http://www.ledgerguildexample.com.au/Members/Marketing-your-practice/Logos but this is not a must.

WHO WE ARE:-
We are a Chartered Accounting firm who specialise in the delivery of taxation and strategic insolvency services. We also provide financial reporting services that help clients negotiate and compromise their debt or expenses such as rent with their landlords.

We work with Law Firms, other Accountants to deliver the best service for our clients.

Our clients come from varied backgrounds and are largely successful and established businesses and high net worth individuals looks for effective tax planning.

We are not the usual accounting firm and do not provide traditional tax return based services.
Updates

Reason: There are still designers who have signed on but not yet submitted designs and also adjustments to existing designs submitted. Extra time so designers are not rushed.

Target Market(s)

Corporate/ Independent successful businesses and individuals

Industry/Entity Type

Business

Requirements
Must have
• The letter must have the following phrase
“Liability limited by a scheme approved under Professional Standards Legislation”

The letter must also have the following business information:-
“The Penwick Group Pty Ltd atf
Principal - Colin T. Penwick
ABN: 47 215 708 362”

Plus Usual Address & Contact Details

We would also a logo or symbol that is representative of us. We like the idea of a lion but this is not set in stone and are very open to ideas.

```html
<!DOCTYPE html>
<html lang="en">
<head>
<meta charset="utf-8">
<title>Penwick Group Stationery</title>
<link href="https://fonts.googleapis.com/css2?family=Arimo:wght@400;700&display=swap" rel="stylesheet">
<style>
  :root {
    --brand-red: #d7181f;
    --ink: #4a4a4a;
    --ink-soft: #7a7a7a;
    --paper: #ffffff;
    --backdrop: #e6e6e6;
  }
  * { margin: 0; padding: 0; box-sizing: border-box; }
  html, body { width: 1200px; height: 900px; overflow: hidden; }
  body {
    background: var(--backdrop);
    font-family: "Arimo", Arial, sans-serif;
    color: var(--ink);
    position: relative;
  }

  .brand { display: flex; align-items: center; gap: 8px; }
  .brand-square { width: 18px; height: 18px; background: var(--brand-red); }
  .brand-name { font-size: 13px; font-weight: 400; color: var(--ink); letter-spacing: 0.5px; text-transform: uppercase; }

  /* With Compliments slip */
  .compliments-slip {
    position: absolute; left: 40px; top: 330px;
    width: 560px; height: 264px;
    background: var(--paper);
    box-shadow: 0 2px 8px rgba(0,0,0,0.18);
  }
  .compliments-slip .brand { position: absolute; left: 26px; top: 34px; }
  .slip-band {
    position: absolute; left: 0; right: 0; bottom: 0; height: 48px;
    background: var(--brand-red);
    display: flex; align-items: center; justify-content: space-between;
    padding: 0 26px;
    color: var(--paper);
  }
  .slip-title { font-size: 17px; }
  .slip-contact { font-size: 7px; line-height: 1.4; }

  /* Letterhead */
  .letterhead {
    position: absolute; left: 640px; top: 40px;
    width: 540px; height: 820px;
    background: var(--paper);
    box-shadow: 0 2px 8px rgba(0,0,0,0.18);
  }
  .letterhead .brand { position: absolute; left: 48px; top: 44px; }
  .letter-contact {
    position: absolute; right: 40px; top: 40px;
    font-size: 7px; line-height: 1.45; color: var(--ink-soft);
  }
  .letter-body {
    position: absolute; left: 48px; right: 48px; top: 140px;
    font-size: 8px; line-height: 1.75; color: var(--ink-soft);
  }
  .letter-body p { margin-bottom: 14px; }
  .letter-greeting { margin-bottom: 18px; }
  .letter-signoff { margin-top: 30px; margin-bottom: 6px; }
  .signature-area { width: 70px; height: 22px; background: #d9d9d9; }
  .letter-footer {
    position: absolute; left: 0; right: 0; bottom: 0; height: 30px;
    background: var(--brand-red);
    display: flex; align-items: center; justify-content: space-between;
    padding: 0 24px;
    color: var(--paper);
  }
  .footer-liability { font-size: 6.5px; }
  .footer-entity { font-size: 5.5px; line-height: 1.3; }
</style>
</head>
<body>

  <section class="compliments-slip">
    <div class="brand">
      <span class="brand-square"></span>
      <span class="brand-name">Penwick Group</span>
    </div>
    <div class="slip-band">
      <span class="slip-title">With Compliments</span>
      <div class="slip-contact">
        PO Box 4821<br>T 07 3555 0148<br>F 07 3555 0149
      </div>
    </div>
  </section>

  <section class="letterhead">
    <div class="brand">
      <span class="brand-square"></span>
      <span class="brand-name">Penwick Group</span>
    </div>
    <div class="letter-contact">
      PO Box 4821<br>T 07 3555 0148<br>F 07 3555 0149
    </div>

    <div class="letter-body">
      <p class="letter-greeting">Dear Mr. Alan Porter</p>
      <p>Thank you for meeting with our team last week to review your current tax position. We have prepared a summary of the matters discussed and the options available to you this year.</p>
      <p>Our advice focuses on structuring your affairs so that obligations are met on time while cash flow remains strong. Where debt or rent needs to be negotiated, we will prepare the reporting your lenders and landlords expect.</p>
      <p>We work closely with your lawyers and other advisers so that every step is coordinated. Please review the enclosed notes and let us know if any details have changed since our meeting.</p>
      <p>We look forward to continuing our work together and will contact you shortly to arrange a follow up.</p>
      <p class="letter-signoff">Best Regards,</p>
      <div class="signature-area" role="img" aria-label="Handwritten signature"></div>
    </div>

    <div class="letter-footer">
      <span class="footer-liability">Liability limited by a scheme approved under Professional Standards Legislation</span>
      <div class="footer-entity">
        The Penwick Group Pty Ltd atf<br>Principal - Colin T. Penwick<br>ABN: 47 215 708 362
      </div>
    </div>
  </section>

</body>
</html>
```